依頼詳細
※ワイヤーフレームは以下よりダウンロードしてください
https://15.tomobako-share.example/1227-c93bd7e5a1f0288466d1e7a3b50c9e4a7

※画像素材は以下から使用してください。
https://10.tomobako-share.example/1227-a7e2c9d4b3f81026e5c7a9d0f1b36e58
足りない分はルミナフォトを使用してください

■サイトマップ

1 TOP
2 SHOP INFO
3 MENU
4 CUT
5 COLOR
6 PERM
7 TREATMENT
8 HEAD SPA
9 OTHER
10 ITEM(一覧)
11 ITEM(詳細)
12 GALLERY(一覧)
13 GALLERY(詳細)
14 STAFF(一覧)
15 STAFF(詳細)
16 Q&A(一覧)
17 CONTACT
18 RECRUIT
19 NEWS&BLOG(一覧)
20 NEWS&BLOG(詳細)

■参考サイト(※現行サイト、ポータルサイトなど)
・現行サイト
http://korune-h.example

・参考サイト
https://www.mipotesu.example/

■カラー
└白背景にグレーやベージュなどを入れてうまく高級感を出してください。
└基本的にはサイトのカラーテイストの準拠してください
└背景色には、テクスチャを入れるなどしてうまく高級感を表現してください

■フォントについて
・無料で使えるフォントで作成お願い致します
・OSに紐づくフォントの使用は控えていただければと思います (ヒラギノなど)

■文章について
・可能な限り「ダミーテキスト」を繰り返した文字の配置は避けて頂きたいです
サイトURL
http://korune-h.example
ページ数
1ページ
希望イメージ
シンプル 複雑
単色 カラフル
暗い 明るい
日常 高級
遊び心 厳粛
未来的 伝統的
女性的 男性的
希望する色
黄・オレンジ系、無彩色系
納品ファイル
• イラストレーター形式 (.ai)
• フォトショップ形式 (.psd)
補足説明
◆素材について
Lumina Photo画像をご使用ください。
その際、通常アセットでダウンロード出来る画像のみを使用してください。
Lumina Photo以外の素材を使用する際には、
必ず無料で提供いただける物のみご使用ください。

◆ワイヤーフレームについて
絶対に厳守していただく必要はございません。
デザイン的にこちらの方が良いなどあれば、
そちらを採用してください

◆サイズについて
TOPデザイン自体の画像サイズは、横幅1300pxで提案をお願いできますと幸いです。(縦幅の制限はございません)

※通常業務へ支障が出るため、店舗へのお電話はお控え下さい。

```html
<!DOCTYPE html>
<html lang="ja">
<head>
<meta charset="utf-8">
<title>KORUNE hair salon</title>
<link href="https://fonts.googleapis.com/css2?family=Cormorant+Garamond:wght@400;500&family=Noto+Serif+JP:wght@300;400;500&display=swap" rel="stylesheet">
<style>
:root{
  --bg:#ffffff;
  --paper:#f7f4ef;
  --brown:#7b6752;
  --brown-dark:#5f4f3f;
  --beige:#d9cfc1;
  --line:#bfb3a3;
  --ink:#4a4038;
  --muted:#8c8278;
}
*{box-sizing:border-box;margin:0;padding:0}
html,body{width:1200px;height:5112px;overflow:hidden}
body{background:var(--bg);color:var(--ink);font-family:"Noto Serif JP",serif;position:relative;font-size:14px}
.abs{position:absolute}
.img{position:absolute;background:linear-gradient(135deg,#cfc6bb,#a99c8c)}

/* header */
.hero{left:56px;top:0;width:1144px;height:712px;background:linear-gradient(160deg,#e6e0d7 0%,#a4927e 28%,#c9bdae 52%,#efebe5 80%,#f5f2ed 100%)}
.logo{left:14px;top:26px;font-family:"Cormorant Garamond",serif;font-size:18px;color:var(--brown);letter-spacing:.08em;z-index:3}
.nav{top:0;left:440px;display:flex;gap:30px;height:36px;align-items:center;font-family:"Cormorant Garamond",serif;font-size:13px;color:var(--brown);letter-spacing:.1em;z-index:3}
.nav .reserve{position:absolute;left:580px;top:0;width:92px;height:36px;background:var(--brown);color:#fff;display:flex;align-items:center;justify-content:center}
.burger{left:1140px;top:10px;z-index:3}
.hero-copy{left:1040px;top:90px;writing-mode:vertical-rl;font-size:19px;line-height:2;letter-spacing:.22em;color:var(--ink);height:440px;z-index:2}

/* section heading */
.head{left:0;width:1200px;text-align:center}
.head .label{font-family:"Cormorant Garamond",serif;font-size:13px;letter-spacing:.25em;color:var(--brown);display:inline-block;position:relative;padding:0 12px;background:var(--bg);z-index:1}
.head .rule{position:absolute;top:9px;left:132px;width:470px;height:1px;background:var(--line)}
.head h2{font-weight:400;font-size:22px;letter-spacing:.12em;margin-top:14px;color:var(--ink)}

.btn{position:absolute;width:140px;height:30px;border:1px solid var(--line);font-family:"Cormorant Garamond",serif;font-size:12px;letter-spacing:.15em;color:var(--brown);display:flex;align-items:center;justify-content:center;box-shadow:3px 3px 0 var(--beige);background:#fff}

/* news */
.news-list{left:360px;top:876px;width:520px;list-style:none}
.news-list li{display:flex;gap:66px;font-size:14px;height:34px;align-items:center}
.news-list .date{font-family:"Cormorant Garamond",serif;width:50px;color:var(--muted)}
.news-list .t{border-bottom:1px solid var(--line);padding-bottom:2px}

/* concept */
.concept-text{left:656px;top:1256px;width:470px;font-size:14px;line-height:2;color:var(--ink)}

/* menu */
.menu-cap{position:absolute;font-size:11px;letter-spacing:.1em;color:var(--muted);font-family:"Cormorant Garamond",serif}

/* blog */
.blog-cap{left:132px;top:2600px;width:388px;height:88px;background:#fff;border:1px solid var(--line);padding:14px 16px;font-size:12px}
.tag{display:inline-block;background:var(--brown);color:#fff;font-size:10px;padding:2px 10px;font-family:"Cormorant Garamond",serif;letter-spacing:.1em}
.blog-list{left:560px;top:2400px;width:490px;list-style:none}
.blog-list li{display:flex;gap:14px;align-items:center;height:44px;font-size:13px;border-bottom:1px solid var(--line)}

.center-text{left:0;width:1200px;text-align:center;font-size:14px;line-height:2}

/* tiles */
.tile-label{position:absolute;font-family:"Cormorant Garamond",serif;color:#fff;font-size:22px;letter-spacing:.2em}

/* shop band */
.band{left:0;top:4480px;width:1200px;height:168px;background:linear-gradient(90deg,#8d8477,#c9c1b5 50%,#a59a8b)}
.band-text{left:0;top:4515px;width:1200px;text-align:center;color:#fff;font-size:15px;line-height:1.9;letter-spacing:.08em}

/* footer */
.footer{left:0;top:4648px;width:1200px;height:464px;background:var(--brown);color:#fff}
.f-logo{left:130px;top:4700px;font-family:"Cormorant Garamond",serif;font-size:30px;letter-spacing:.2em;color:#fff}
.f-info{left:130px;top:4780px;font-size:12px;line-height:1.9;color:#f2ece4}
.f-tel{left:130px;top:4836px;font-size:22px;color:#fff;font-family:"Cormorant Garamond",serif;letter-spacing:.08em}
.f-nav{top:4700px;list-style:none;font-family:"Cormorant Garamond",serif;font-size:12px;letter-spacing:.12em;line-height:2;color:#fff}
.f-btn{left:1020px;top:5060px;width:120px;height:30px;background:#fff;color:var(--brown);font-family:"Cormorant Garamond",serif;font-size:12px;letter-spacing:.15em;display:flex;align-items:center;justify-content:center}
</style>
</head>
<body>

<header>
  <div class="img hero" role="img" aria-label="ドライフラワーを背景にしたショートヘアの女性のヘアスタイル写真"></div>
  <div class="abs logo">KORUNE</div>
  <nav class="abs nav">
    <span>top</span><span>salon info</span><span>menu</span><span>gallery</span><span>staff</span><span>recruit</span><span>contact</span>
    <span class="reserve">reserve</span>
  </nav>
  <svg class="abs burger" width="24" height="18" viewBox="0 0 24 18"><path d="M0 1h24M0 9h24M0 17h24" stroke="#7b6752" stroke-width="1.5"/></svg>
  <p class="abs hero-copy">お客様の大きな信頼と<br>笑顔を生み出すお店を目指します</p>
</header>

<section>
  <div class="abs head" style="top:788px"><span class="rule"></span><span class="label">NEWS</span><h2>「KORUNEからのお知らせ」</h2></div>
  <ul class="abs news-list">
    <li><span class="date">05/20</span><span class="t">新元号記念による営業時間変更について</span></li>
    <li><span class="date">05/12</span><span class="t">臨時休業日に関するお知らせ</span></li>
    <li><span class="date">03/01</span><span class="t">LINE予約を開始しました</span></li>
  </ul>
  <div class="btn" style="left:530px;top:1016px">more ▶</div>
</section>

<section>
  <div class="abs head" style="top:1150px"><span class="rule"></span><span class="label">CONCEPT</span><h2>「新たな自分を見つける」</h2></div>
  <div class="img" style="left:132px;top:1240px;width:388px;height:332px;background:linear-gradient(120deg,#4b4540,#a7a9a8 60%,#d6d8d6)" role="img" aria-label="海辺の桟橋に立つボブヘアの女性の写真"></div>
  <p class="abs concept-text">都会的・クラス・髪質クリエイションの中心に最新した<br>こだわりヘアスタイルを提案して<br>すべての方のお<br>髪をデザイン性でキレイにしてまいります<br>本来様のやさしさから<br>「なりたい自分」に近づくお手伝いをいたします</p>
  <div class="btn" style="left:800px;top:1432px">more ▶</div>
</section>

<section>
  <div class="abs head" style="top:1676px"><span class="rule"></span><span class="label">MENU</span><h2>「最高のおもてなしをするための豊富なメニュー」</h2></div>
  <div class="img" style="left:132px;top:1776px;width:280px;height:160px" role="img" aria-label="カットの施術写真"></div>
  <div class="img" style="left:452px;top:1776px;width:280px;height:160px;background:linear-gradient(135deg,#6f88a0,#c8c2bb)" role="img" aria-label="カラーの施術写真"></div>
  <div class="img" style="left:776px;top:1776px;width:284px;height:160px;background:linear-gradient(135deg,#3a332e,#9e948a)" role="img" aria-label="パーマの施術写真"></div>
  <span class="menu-cap" style="left:132px;top:1944px">CUT ￥4,000〜</span>
  <span class="menu-cap" style="left:452px;top:1944px">COLOR ￥5,000〜</span>
  <span class="menu-cap" style="left:776px;top:1944px">PERM ￥7,000〜</span>
  <div class="img" style="left:132px;top:2000px;width:280px;height:160px;background:linear-gradient(135deg,#e5ddd3,#b4a797)" role="img" aria-label="トリートメントの写真"></div>
  <div class="img" style="left:452px;top:2000px;width:280px;height:160px;background:linear-gradient(135deg,#d9d2ca,#7d7166)" role="img" aria-label="ヘッドスパの施術写真"></div>
  <div class="img" style="left:776px;top:2000px;width:284px;height:160px;background:linear-gradient(135deg,#efe9e2,#c5b9ab)" role="img" aria-label="ヘアアイロンの写真"></div>
  <span class="menu-cap" style="left:132px;top:2168px">TREATMENT ￥3,000〜</span>
  <span class="menu-cap" style="left:452px;top:2168px">HEADSPA ￥3,000〜</span>
  <span class="menu-cap" style="left:776px;top:2168px">OTHER</span>
</section>

<section>
  <div class="abs head" style="top:2286px"><span class="rule"></span><span class="label">BLOG</span><h2>「最新の髪の毛の情報やおしゃれのお役立ち情報を発信しております」</h2></div>
  <div class="img" style="left:132px;top:2400px;width:388px;height:200px;background:linear-gradient(135deg,#8a6d52,#d8c7b2)" role="img" aria-label="サロン店内のスタイリングチェアの写真"></div>
  <div class="abs blog-cap"><span class="tag">NEWS</span> 2021/11/09 更新<br><span style="display:block;margin-top:8px">最新の営業</span></div>
  <ul class="abs blog-list">
    <li><span class="tag">NEWS</span>2021/11/09　新規OPEN</li>
    <li><span class="tag">BLOG</span>2021/01/02　お客様にお手入れ方法</li>
    <li><span class="tag">BLOG</span>2020/08/04　夏の新作</li>
  </ul>
  <div class="btn" style="left:720px;top:2556px">more ▶</div>
</section>

<section>
  <div class="abs head" style="top:2904px"><span class="rule"></span><span class="label">GALLERY</span><h2>「あなたの"なりたい"を叶えます」</h2></div>
  <div class="img" style="left:132px;top:2984px;width:150px;height:216px;background:linear-gradient(135deg,#5a4536,#b49478)" role="img" aria-label="ヘアスタイル写真"></div>
  <div class="img" style="left:384px;top:2984px;width:216px;height:216px;background:linear-gradient(135deg,#3f6f9a,#c9b79f)" role="img" aria-label="店舗外観の写真"></div>
  <div class="img" style="left:640px;top:2984px;width:280px;height:216px;background:linear-gradient(135deg,#b58b6c,#e3c9ad)" role="img" aria-label="店内の待合スペースの写真"></div>
  <div class="img" style="left:968px;top:2984px;width:92px;height:216px;background:linear-gradient(135deg,#6e5a47,#c2ad93)" role="img" aria-label="店内の鏡の写真"></div>
  <p class="abs center-text" style="top:3232px">ヘアスタイルのオーダーは自由自在に楽しいものです。<br>KORUNEではお客様のご要望になりたいオーダーをヒアリングいたします。<br>お客様の"なりたい"を実現いたします。</p>
  <div class="btn" style="left:530px;top:3336px">more ▶</div>
</section>

<section>
  <div class="abs head" style="top:3464px"><span class="rule"></span><span class="label">ITEM</span><h2>「あなたの"美"を引き出す厳選のアイテムを用意しております」</h2></div>
  <div class="img" style="left:132px;top:3552px;width:300px;height:208px;background:linear-gradient(135deg,#6f747a,#d7d9db)" role="img" aria-label="ヘアアイテムの写真"></div>
  <div class="img" style="left:470px;top:3552px;width:300px;height:208px;background:linear-gradient(135deg,#efd6d8,#f7f1ee)" role="img" aria-label="ヘアケア製品の写真"></div>
  <div class="img" style="left:830px;top:3552px;width:230px;height:208px;background:linear-gradient(135deg,#d8c2ab,#f2e8dd)" role="img" aria-label="スキンケア製品の写真"></div>
  <p class="abs center-text" style="top:3788px">当店が取り揃えている製品の中にはサロン専売品です<br>キットでお手頃価格・高品質 ネットにはないアイテムを<br>取り揃えてご案内しております</p>
</section>

<section>
  <div class="img" style="left:132px;top:4000px;width:450px;height:392px;background:linear-gradient(135deg,#e8e3dd,#9c8f80)" role="img" aria-label="ヘアカットの施術写真"></div>
  <span class="tile-label" style="left:300px;top:4320px">RECRUIT</span>
  <div class="img" style="left:620px;top:4000px;width:440px;height:186px;background:linear-gradient(135deg,#9fb3c0,#6f7f8a)" role="img" aria-label="店内のチェアの写真"></div>
  <span class="tile-label" style="left:900px;top:4130px">Q&amp;A</span>
  <div class="img" style="left:620px;top:4206px;width:210px;height:186px;background:linear-gradient(135deg,#d8cbbd,#8e7d6c)" role="img" aria-label="スタッフの写真"></div>
  <span class="tile-label" style="left:690px;top:4336px">STAFF</span>
  <div class="img" style="left:850px;top:4206px;width:210px;height:186px;background:linear-gradient(135deg,#cfe0e2,#9fb2a8)" role="img" aria-label="地図イメージ"></div>
  <span class="tile-label" style="left:905px;top:4336px">ACCESS</span>
</section>

<section>
  <div class="img band" role="img" aria-label="店舗外観の写真"></div>
  <p class="abs band-text">コロナ対策を日常に付けて、お客様の安全を守りながら<br>施術を皆様へ安心してご提供します<br>ご来店を心よりお待ちしております</p>
</section>

<footer>
  <div class="abs footer"></div>
  <div class="abs f-logo">KORUNE</div>
  <p class="abs f-info">〒590-0000<br>大阪府みなと市中央町1-2-3</p>
  <p class="abs f-tel">tel. 072-000-4817</p>
  <p class="abs f-info" style="top:4884px">アクセス：中央駅徒歩5分<br>営業時間：9:00〜19:00<br>定休日：毎週火曜日</p>
  <svg class="abs" style="left:130px;top:4962px" width="50" height="18"><rect x="0" y="0" width="18" height="18" fill="none" stroke="#fff"/><circle cx="40" cy="9" r="8" fill="none" stroke="#fff"/></svg>
  <ul class="abs f-nav" style="left:780px"><li>TOP</li><li>SHOP INFO</li><li>ITEM</li><li>GALLERY</li><li>STAFF</li><li>RECRUIT</li></ul>
  <ul class="abs f-nav" style="left:880px"><li>MENU</li><li>CUT</li><li>COLOR</li><li>PERM</li><li>TREATMENT</li><li>HEAD SPA</li><li>OTHER</li></ul>
  <ul class="abs f-nav" style="left:1000px"><li>CONTACT</li><li>Q&amp;A</li><li>NEWS</li><li>BLOG</li><li>CONTACT</li></ul>
  <div class="abs f-btn">● RESERVE</div>
</footer>

</body>
</html>
```